Revamp PowerPoint deck to match our new website's visual identity and effectively tell our story

Revamp PowerPoint Deck to Match New Corporate Website Theme @ https://tovelrin4.qx-stage.com/.
(Note: The content on the new theme is placeholder text. The current live website is www.brelvoxa.com )

Key Request: Slide Master SHOULD NOT include any specific contents. It should contain only essential elements such master layout, the logo, header, footer, and any repeating text elements and it should be limited to a maximum of 5 pages.

We need to redesign our existing PowerPoint deck to align with the visual identity of our new corporate website while ensuring it effectively tells our story. The revamped deck should focus on:

1. Visual Storytelling: Each slide should guide the audience through a clear and compelling narrative. Build on each slide to ensure the story flows seamlessly.

2. Minimal Text, More Visuals: Avoid text-heavy slides. Where text is necessary, keep it concise. Focus on strong visuals, icons, and imagery that reinforce key points. Ensure the visuals are impactful and align with our brand identity. Use bold icons and high-quality images that match the tone of the new website to emphasize key messages.

3. Design Consistency: Ensure the presentation reflects the color palette, typography, and imagery from the new website. This includes maintaining consistency in the style of headings, subheadings, and body text to reinforce our brand identity.

4. Modern & Clean Design: Embrace a minimalist design aesthetic inspired by the new website. Use the same color schemes, fonts, and clean layouts to ensure the slides are visually engaging and easy to digest.

5. Professional, Minimalist Look: Keep the design professional and minimalist, with a focus on clarity. Ensure each slide conveys its message clearly without unnecessary distractions.

Our goal is to create a visually engaging and interactive presentation that clearly communicates our message while keeping the audience engaged.

Ensure our corporate color scheme is maintained as per the current website: www.brelvoxa.com

Target Market(s)

B2B Clients in Asia Pacific and Australia

Industry/Entity Type

Across all industries, but more specific to IT

Requirements
Must have
• nsure our corporate color scheme is maintained as per the current website: www.brelvoxa.com
Nice to have
• More graphics and illustrations than text. Icon representations.
Should not have
• Slide Master SHOULD NOT include any specific contents. It should contain only essential elements such master layout, the logo, header, footer, and any repeating text elements and it should be limited to a maximum of 5 pages

```html
<!DOCTYPE html>
<html lang="en">
<head>
<meta charset="utf-8">
<title>Brelvoxa – Presentation Deck</title>
<link href="https://fonts.googleapis.com/css2?family=Roboto:wght@400;500;700&family=Roboto+Condensed:wght@500;700&family=Anton&display=swap" rel="stylesheet">
<style>
:root{
  --red:#d0312d;
  --slate:#5b6880;
  --slate-dark:#485670;
  --slate-soft:#7c839c;
  --sky:#e3ebfb;
  --pink:#fbd8d8;
  --orange:#e8501e;
  --cyan:#1fc0d9;
  --ink:#222428;
  --body:#555a62;
  --rule:#5b6880;
  --canvas:#b9b9b9;
  --chip:#f2f2f2;
}
*{margin:0;padding:0;box-sizing:border-box}
html,body{width:811px;height:1200px;overflow:hidden;background:var(--canvas)}
body{font-family:"Roboto",Arial,sans-serif;color:var(--ink)}
.sheet{position:absolute;left:0;top:0;width:1570px;height:2324px;transform:scale(0.51656);transform-origin:0 0;background:var(--canvas)}
.slide{position:absolute;width:712px;height:401px;background:#fff;overflow:hidden}
.abs{position:absolute}
.svg-layer{position:absolute;left:0;top:0}
.brand{position:absolute;font-family:"Roboto",Arial,sans-serif;font-weight:700;color:var(--red);letter-spacing:2px;font-size:13px;line-height:1}
.footer .brand{left:17px;top:376px}
.footer-rule{position:absolute;left:121px;top:384px;width:516px;height:2px;background:var(--rule)}
.page-tab{position:absolute;left:660px;top:362px;width:32px;height:40px;background:var(--red);border-radius:16px 16px 0 0;color:#fff;font-size:9px;text-align:center;padding-top:16px}
.heading{font-family:"Roboto Condensed",Arial,sans-serif;font-weight:700;font-size:26px;letter-spacing:.3px;color:var(--ink)}
.heading.center{position:absolute;left:0;width:712px;text-align:center}
/* cover */
.cover-kicker{left:44px;top:127px;font-size:11px}
.cover-title{left:43px;top:154px;font-size:22.5px;font-weight:500;line-height:26px}
.cover-contact{left:44px;font-size:11px;display:flex;align-items:center;gap:14px}
.cover-copy{left:42px;top:366px;font-size:9.5px}
.cover-art{position:absolute;left:314px;top:36px;width:398px;height:365px;background:linear-gradient(135deg,var(--sky) 0%,var(--slate) 45%,var(--red) 100%)}
/* usage cards */
.usage-sub{position:absolute;left:0;width:712px;top:68px;text-align:center;font-size:14.5px}
.usage-card{position:absolute;width:198px;height:110px;background:#fff;border-top:3px solid var(--red);border-radius:3px;box-shadow:0 3px 10px rgba(0,0,0,.12)}
.usage-card svg{position:absolute;left:12px;top:12px}
.usage-card h3{position:absolute;left:58px;top:22px;font-size:14.5px;font-weight:400}
.usage-card p{position:absolute;left:58px;top:46px;width:128px;font-size:7.3px;line-height:11px;color:var(--body)}
/* about */
.about-copy{position:absolute;left:41px;width:640px;font-size:9.3px;line-height:15px}
.stat{position:absolute;width:120px;height:140px;text-align:center}
.stat svg{position:absolute;left:0;top:0}
.stat-num{position:absolute;left:0;width:120px;font-size:20px;font-weight:700;color:var(--red)}
.stat-label{position:absolute;left:-10px;width:140px;top:113px;font-size:9.5px;line-height:15px;color:var(--ink)}
/* ccx */
.ccx-title{position:absolute;top:265px;font-size:14px;font-weight:500}
.ccx-text{position:absolute;top:290px;width:145px;font-size:8.7px;line-height:16.5px;color:var(--ink)}
/* pillars */
.pillar-label{position:absolute;font-size:9px;text-align:center}
.pillar-num{position:absolute;left:407px;font-size:23px;font-weight:500}
.pillar-title{position:absolute;left:448px;font-size:8.7px;font-weight:700}
.pillar-text{position:absolute;left:448px;width:225px;font-size:6.9px;line-height:11px;color:var(--body)}
/* event */
.event-title{position:absolute;left:0;width:712px;top:24px;text-align:center;font-size:22.5px;font-weight:500;line-height:26px;letter-spacing:.4px}
.event-box{position:absolute;width:285px;height:86px;border:1.5px solid #d9d9d9;background:#fff}
.event-no{position:absolute;left:12px;top:10px;width:33px;height:33px;border-radius:50%;background:var(--red);color:#fff;font-size:10px;font-weight:500;text-align:center;line-height:33px}
.event-box h4{position:absolute;left:56px;top:10px;width:215px;font-size:10px;font-weight:500;line-height:13.5px}
.event-box p{position:absolute;left:57px;width:215px;font-size:7px;line-height:13.5px;color:var(--body)}
/* solution */
.sol-title{position:absolute;font-size:11px;font-weight:500;line-height:14.5px}
.sol-text{position:absolute;width:135px;font-size:7.8px;line-height:15px;color:var(--body)}
.right{text-align:right}
/* thank you */
.thanks-band{position:absolute;left:0;top:0;width:712px;height:351px;background:var(--slate)}
.thanks-word{position:absolute;left:40px;top:22px;font-family:"Anton",Impact,sans-serif;font-size:106px;letter-spacing:8px;line-height:1;background:linear-gradient(180deg,#ffffff 15%,rgba(255,255,255,.05) 95%);-webkit-background-clip:text;background-clip:text;color:transparent}
.thanks-pill{position:absolute;left:0;top:185px;width:302px;height:136px;background:var(--slate-dark);border-radius:0 68px 68px 0}
.thanks-line{position:absolute;left:110px;font-size:11px;font-weight:500;color:#fff;line-height:13px}
.thanks-ico{position:absolute;left:82px}
.thanks-art{position:absolute;left:335px;top:85px;width:340px;height:250px;background:linear-gradient(135deg,#eef0f8 0%,#c4c9dc 55%,var(--red) 100%)}
</style>
</head>
<body>
<div class="sheet">

<section class="slide" style="left:49px;top:58px">
  <div class="brand" style="left:44px;top:32px">BRELVOXA</div>
  <div class="abs cover-kicker">Integrated CX Solutions:</div>
  <h1 class="abs cover-title">Data-Led, Content<br>Driven, Contact<br>Center Empowered</h1>
  <div class="abs cover-contact" style="top:253px">
    <svg width="11" height="9" viewBox="0 0 11 9"><rect width="11" height="9" rx="1" fill="var(--red)"/><path d="M0.5 1 5.5 5 10.5 1" stroke="#fff" fill="none"/></svg>
    <span>enquiries@brelvoxa.com</span>
  </div>
  <div class="abs cover-contact" style="top:279px">
    <svg width="11" height="11" viewBox="0 0 24 24"><path fill="var(--red)" d="M6.6 10.8a15 15 0 0 0 6.6 6.6l2.2-2.2c.3-.3.7-.4 1-.2 1.1.4 2.3.6 3.6.6.6 0 1 .4 1 1V20c0 .6-.4 1-1 1A17 17 0 0 1 3 4c0-.6.4-1 1-1h3.5c.6 0 1 .4 1 1 0 1.3.2 2.5.6 3.6.1.3 0 .7-.2 1z"/></svg>
    <span>+1 555 010 0100</span>
  </div>
  <div class="abs cover-copy">© &nbsp;Copyrights 2024 | All Rights Reserved</div>
  <div class="cover-art" role="img" aria-label="Geometric composition of red, slate, pink and light blue squares, circles and quarter circles"></div>
</section>

<section class="slide" style="left:808px;top:58px">
  <svg class="svg-layer" width="712" height="401"><circle cx="100" cy="-8" r="112" fill="var(--sky)"/><circle cx="100" cy="-8" r="60" fill="#fff"/></svg>
  <h2 class="heading center" style="top:28px">USAGE OF DATA</h2>
  <p class="usage-sub">Brelvo data can be a functional asset for organisation in the areas of:</p>
  <div class="usage-card" style="left:41px;top:110px">
    <svg width="34" height="34" viewBox="0 0 34 34"><path d="M17 2l4 3 5-1 1 5 4 3-2 5 2 5-4 3-1 5-5-1-4 3-4-3-5 1-1-5-4-3 2-5-2-5 4-3 1-5 5 1z" fill="var(--red)"/><circle cx="13" cy="13" r="2.5" fill="#fff"/><circle cx="21" cy="21" r="2.5" fill="#fff"/><path d="M22 11 12 23" stroke="#fff" stroke-width="2"/></svg>
    <h3>Sales</h3><p>Lorem ipsum dolor sit amet, conse ctetur adipiscing elit, sed do eiusm od tempor incididunt ut labore et dolore magna aliqua.</p>
  </div>
  <div class="usage-card" style="left:257px;top:110px">
    <svg width="34" height="34" viewBox="0 0 34 34"><path d="M6 20l14-12 4 14-10-1z" fill="var(--red)"/><path d="M9 21l3 9h4l-2-8" fill="var(--red)"/><path d="M25 6l3-3M27 12h4M23 2l1 3" stroke="var(--red)" stroke-width="2"/></svg>
    <h3>Marketing</h3><p>Lorem ipsum dolor sit amet, conse ctetur adipiscing elit, sed do eiusm od tempor incididunt ut labore et dolore magna aliqua.</p>
  </div>
  <div class="usage-card" style="left:473px;top:110px">
    <svg width="34" height="34" viewBox="0 0 34 34"><rect x="18" y="2" width="13" height="16" rx="1" fill="var(--red)"/><rect x="3" y="18" width="11" height="13" rx="1" fill="var(--red)"/><path d="M6 14V8h8M28 22v6h-9" stroke="var(--red)" stroke-width="2" fill="none"/><path d="M21 7h7M21 11h7" stroke="#fff" stroke-width="1.5"/></svg>
    <h3>Append &amp; Enrich</h3><p>Lorem ipsum dolor sit amet, conse ctetur adipiscing elit, sed do eiusm od tempor incididunt ut labore et dolore magna aliqua.</p>
  </div>
  <div class="usage-card" style="left:41px;top:236px">
    <svg width="34" height="34" viewBox="0 0 34 34"><circle cx="12" cy="10" r="7" fill="var(--red)"/><path d="M1 30c0-8 5-12 11-12s8 2 9 4v8z" fill="var(--red)"/><circle cx="24" cy="22" r="5" fill="none" stroke="var(--red)" stroke-width="2.5"/><path d="M27.5 25.5 32 30" stroke="var(--red)" stroke-width="3"/></svg>
    <h3>Recruiting</h3><p>Lorem ipsum dolor sit amet, conse ctetur adipiscing elit, sed do eiusm od tempor incididunt ut labore et dolore magna aliqua.</p>
  </div>
  <div class="usage-card" style="left:257px;top:236px">
    <svg width="34" height="34" viewBox="0 0 34 34"><circle cx="21" cy="12" r="10" fill="var(--red)"/><path d="M17 16v-4M21 16V8M25 16v-6" stroke="#fff" stroke-width="2"/><path d="M13 20 3 30" stroke="var(--red)" stroke-width="4" stroke-linecap="round"/></svg>
    <h3>Research</h3><p>Lorem ipsum dolor sit amet, conse ctetur adipiscing elit, sed do eiusm od tempor incididunt ut labore et dolore magna aliqua.</p>
  </div>
  <div class="usage-card" style="left:473px;top:236px">
    <svg width="34" height="34" viewBox="0 0 34 34"><rect x="3" y="20" width="5" height="11" fill="var(--red)"/><rect x="11" y="15" width="5" height="16" fill="var(--red)"/><rect x="19" y="18" width="5" height="13" fill="var(--red)"/><rect x="27" y="9" width="5" height="22" fill="var(--red)"/><path d="M3 14l9-7 7 5 11-9" stroke="var(--red)" stroke-width="2" fill="none"/></svg>
    <h3>Analysis</h3><p>Lorem ipsum dolor sit amet, conse ctetur adipiscing elit, sed do eiusm od tempor incididunt ut labore et dolore magna aliqua.</p>
  </div>
  <div class="footer"><div class="brand">BRELVOXA</div><div class="footer-rule"></div><div class="page-tab">05</div></div>
</section>

<section class="slide" style="left:49px;top:506px">
  <h2 class="heading abs" style="left:41px;top:17px">ABOUT US</h2>
  <p class="about-copy" style="top:62px">Brelvoxa empowers industry-leading brands with cutting-edge, data-driven CX solutions that seamlessly integrates data intelligence, compelling content, and expert insights with localised contact center to drive success across the Asia Pacific and Oceania regions.</p>
  <p class="about-copy" style="top:107px">We enable brands to efficiently acquire new customers and maintain exceptional customer experiences through state-of-the-art, tailored marketing strategies uniquely designed to meet specific business goals.</p>
  <div class="stat" style="left:43px;top:171px">
    <svg width="120" height="120"><circle cx="60" cy="60" r="45" fill="var(--chip)"/><path d="M6 60A54 54 0 0 1 114 60" stroke="var(--red)" stroke-width="9" fill="none"/></svg>
    <div class="stat-num" style="top:48px">2010</div><div class="stat-label">YEAR ESTABLISHED</div>
  </div>
  <div class="stat" style="left:171px;top:171px">
    <svg width="120" height="120"><circle cx="60" cy="60" r="45" fill="var(--chip)"/><path d="M6 60A54 54 0 0 0 114 60" stroke="var(--slate)" stroke-width="9" fill="none"/></svg>
    <div class="stat-num" style="top:36px">8</div><div class="stat-label">REGIONAL OFFICES</div>
  </div>
  <div class="stat" style="left:299px;top:171px">
    <svg width="120" height="120"><circle cx="60" cy="60" r="45" fill="var(--chip)"/><path d="M6 60A54 54 0 0 1 114 60" stroke="var(--red)" stroke-width="9" fill="none"/></svg>
    <div class="stat-num" style="top:48px">200+</div><div class="stat-label">EMPLOYEES</div>
  </div>
  <div class="stat" style="left:428px;top:171px">
    <svg width="120" height="120"><circle cx="60" cy="60" r="45" fill="var(--chip)"/><path d="M6 60A54 54 0 0 0 114 60" stroke="var(--slate)" stroke-width="9" fill="none"/></svg>
    <div class="stat-num" style="top:36px">10M+</div><div class="stat-label">B2B DATA ACCESS</div>
  </div>
  <div class="stat" style="left:555px;top:171px">
    <svg width="120" height="120"><circle cx="60" cy="60" r="45" fill="var(--chip)"/><path d="M6 60A54 54 0 0 1 114 60" stroke="var(--red)" stroke-width="9" fill="none"/></svg>
    <div class="stat-num" style="top:48px">200+</div><div class="stat-label">REGIONAL AND<br>GLOBAL CLIENTS</div>
  </div>
  <div class="footer"><div class="brand">BRELVOXA</div><div class="footer-rule"></div><div class="page-tab">02</div></div>
</section>

<section class="slide" style="left:808px;top:506px">
  <h2 class="heading center" style="top:30px">CCX - VALUE PROPOSITION</h2>
  <svg class="svg-layer" width="712" height="401">
    <line x1="15" y1="231" x2="672" y2="231" stroke="var(--slate)" stroke-width="1.5" stroke-dasharray="1.5 4"/>
    <g fill="none" stroke-width="5">
      <circle cx="101" cy="144" r="58" stroke="#ececec"/>
      <circle cx="101" cy="144" r="58" stroke="var(--red)" stroke-dasharray="280 365" transform="rotate(-95 101 144)"/>
      <circle cx="254" cy="144" r="58" stroke="#ececec"/>
      <circle cx="254" cy="144" r="58" stroke="var(--slate)" stroke-dasharray="150 365"/>
      <circle cx="405" cy="144" r="58" stroke="#ececec"/>
      <circle cx="405" cy="144" r="58" stroke="var(--red)" stroke-dasharray="300 365" transform="rotate(-100 405 144)"/>
      <circle cx="576" cy="144" r="58" stroke="#ececec"/>
      <circle cx="576" cy="144" r="58" stroke="var(--slate)" stroke-dasharray="250 365" transform="rotate(190 576 144)"/>
    </g>
    <circle cx="101" cy="144" r="42" fill="var(--red)"/>
    <rect x="87" y="125" width="26" height="34" rx="3" fill="#fff"/>
    <path d="M92 133h16M92 139h16M92 145h12M92 151h9" stroke="var(--red)" stroke-width="2"/>
    <path d="M108 158l10-14 4 3-10 14-5 1z" fill="#fff"/>
    <circle cx="246" cy="125" r="6" fill="var(--slate)"/><circle cx="263" cy="125" r="6" fill="var(--slate)"/>
    <path d="M236 141c0-7 20-7 20 0zM253 141c0-7 20-7 20 0z" fill="var(--slate)"/>
    <path d="M236 144h37l-13 12v10h-11v-10z" fill="var(--slate)"/>
    <circle cx="405" cy="144" r="42" fill="var(--red)"/>
    <path d="M390 158l18-28 10 14z" fill="#fff"/><path d="M392 160l6 6" stroke="#fff" stroke-width="5"/>
    <path d="M416 130l4-5M422 140h6M419 134l5-2" stroke="#fff" stroke-width="2"/>
    <rect x="552" y="127" width="48" height="38" rx="6" fill="var(--slate)"/>
    <path d="M564 122v10M588 122v10" stroke="var(--slate)" stroke-width="4"/>
    <rect x="552" y="127" width="48" height="8" fill="var(--slate-dark)"/>
    <path d="M576 138l3 6 6 1-5 4 1 6-5-3-5 3 1-6-5-4 6-1z" fill="#fff"/>
    <circle cx="52" cy="231" r="6" fill="var(--red)"/><circle cx="205" cy="231" r="6" fill="var(--slate)"/>
    <circle cx="360" cy="231" r="6" fill="var(--red)"/><circle cx="528" cy="231" r="6" fill="var(--slate)"/>
  </svg>
  <div class="ccx-title" style="left:35px">Content Syndication</div>
  <p class="ccx-text" style="left:36px">Leveraging the power of Link CX, we deliver your content in versatile, interactive formats</p>
  <div class="ccx-title" style="left:198px">Lead Generation</div>
  <p class="ccx-text" style="left:199px">By leveraging the Link CX platform, we precisely identify and target key companies and</p>
  <div class="ccx-title" style="left:352px">Advertising</div>
  <p class="ccx-text" style="left:353px">Link CX amplifies your reach across Asia Pacific, Oceania, and beyond. We enhance customer</p>
  <div class="ccx-title" style="left:522px">Events</div>
  <p class="ccx-text" style="left:523px">Leveraging the extensive reach of Link CX, we efficiently attract attendees for both in-person and</p>
  <div class="footer"><div class="brand">BRELVOXA</div><div class="footer-rule"></div><div class="page-tab">06</div></div>
</section>

<section class="slide" style="left:49px;top:954px">
  <svg class="svg-layer" width="712" height="401"><circle cx="611" cy="30" r="102" fill="var(--sky)"/><circle cx="611" cy="30" r="42" fill="#fff"/></svg>
  <h2 class="heading abs" style="left:41px;top:24px">OUR FOUR CORE PILERS</h2>
  <svg class="svg-layer" width="712" height="401" fill="none" stroke-width="6">
    <path d="M78 116H180a31 31 0 0 1 31 31V200H109a31 31 0 0 1 -31 -31Z" stroke="var(--orange)"/>
    <path d="M226 146H340V217H254a28 28 0 0 1 -28 -28V174a28 28 0 0 1 28 -28Z" stroke="var(--slate)"/>
    <path d="M47 215H174a31 31 0 0 1 31 31V315H78a31 31 0 0 1 -31 -31Z" stroke="var(--slate)"/>
    <path d="M222 235H350V315H253a31 31 0 0 1 -31 -31V266a31 31 0 0 1 31 -31Z" stroke="var(--orange)"/>
    <g stroke="none" fill="var(--orange)">
      <rect x="132" y="152" width="4" height="10"/><rect x="139" y="147" width="4" height="15"/><rect x="146" y="150" width="4" height="12"/><rect x="153" y="143" width="4" height="19"/>
      <path d="M131 148l8-6 6 4 9-7" stroke="var(--orange)" stroke-width="1.5" fill="none"/>
      <circle cx="285" cy="271" r="9"/><circle cx="278" cy="274" r="6"/><circle cx="293" cy="274" r="6"/><rect x="276" y="274" width="18" height="6"/>
      <path d="M280 281v6M285 281v9M290 281v6" stroke="var(--orange)" stroke-width="1.5"/>
    </g>
    <g stroke="none" fill="var(--slate)">
      <path d="M274 172a9 9 0 0 1 18 0" stroke="var(--slate)" stroke-width="2.5" fill="none"/>
      <rect x="271" y="170" width="5" height="9" rx="2"/><rect x="290" y="170" width="5" height="9" rx="2"/>
      <circle cx="126" cy="247" r="3.5"/><circle cx="117" cy="260" r="3.5"/><circle cx="126" cy="260" r="3.5"/><circle cx="135" cy="260" r="3.5"/>
      <path d="M126 251v5M117 256h18" stroke="var(--slate)" stroke-width="1.5"/>
      <rect x="113" y="265" width="8" height="3"/><rect x="122" y="265" width="8" height="3"/><rect x="131" y="265" width="8" height="3"/>
    </g>
  </svg>
  <div class="pillar-label" style="left:117px;top:171px;width:56px">DATA</div>
  <div class="pillar-label" style="left:236px;top:192px;width:100px">CONTACT CENTRE</div>
  <div class="pillar-label" style="left:86px;top:282px;width:80px">LINKCX</div>
  <div class="pillar-label" style="left:237px;top:286px;width:100px">DIGITAL CHANNEL</div>
  <div class="pillar-num" style="top:110px">01</div>
  <div class="pillar-title" style="top:114px">Data-led Conversations With Potential Buyers</div>
  <p class="pillar-text" style="top:128px">Data is at the heart of our expertise. We specialize in guiding you through the process of acquiring the precise data you need.</p>
  <div class="pillar-num" style="top:166px;color:var(--orange)">02</div>
  <div class="pillar-title" style="top:170px">Driving Results Through Deep Customer Experience</div>
  <p class="pillar-text" style="top:184px">Our hyper-localized contact centers are laser-focused on delivering exceptional customer experiences daily.</p>
  <div class="pillar-num" style="top:222px">03</div>
  <div class="pillar-title" style="top:226px">Harness The Power with AI Enhanced Content Channel</div>
  <p class="pillar-text" style="top:240px">IT decision-makers rely on the latest industry insights and technology updates, keeping LinkCX's audience engaged and</p>
  <div class="pillar-num" style="top:277px;color:var(--orange)">04</div>
  <div class="pillar-title" style="top:282px">Precision Marketing Through Advanced Digital Channels.</div>
  <p class="pillar-text" style="top:296px">Our sophisticated digital channel partnerships and technologies, combined with our experience, ensure that the right marketing messages reach</p>
  <div class="footer"><div class="brand">BRELVOXA</div><div class="footer-rule"></div><div class="page-tab">03</div></div>
</section>

<section class="slide" style="left:808px;top:954px">
  <h2 class="event-title">MAXIMIZING EVENT SUCCESS WITH<br>TARGETED ENGAGEMENT</h2>
  <div class="event-box" style="left:64px;top:89px"><div class="event-no">01</div><h4>Precisely Identify Your Event's<br>Target Audience</h4><p style="top:43px">We pinpoint the ideal attendees to ensure your event reaches those who matter most.</p></div>
  <div class="event-box" style="left:364px;top:89px"><div class="event-no">02</div><h4>Craft Compelling Event Landing Pages</h4><p style="top:29px">We design comprehensive landing pages featuring the event agenda, speaker profiles, and a streamlined registration process.</p></div>
  <div class="event-box" style="left:64px;top:186px"><div class="event-no">03</div><h4>Implement Multi-Touchpoint<br>Engagement Strategies</h4><p style="top:43px">We create multiple engagement touch points to ensure no key personas are overlooked.</p></div>
  <div class="event-box" style="left:364px;top:186px"><div class="event-no">04</div><h4 style="top:7px">Extend Invitations Through<br>Multiple Channels</h4><p style="top:38px">We deliver personalized invitations via email, SMS, chat apps, social networks, and through our efficient contact center.</p></div>
  <div class="event-box" style="left:214px;top:284px"><div class="event-no">05</div><h4>Amplify Event Visibility Through<br>Our Content Platform</h4><p style="top:41px">We promote your event on our content platform to maximize reach and engage a broader audience..</p></div>
  <div class="footer"><div class="brand">BRELVOXA</div><div class="footer-rule"></div><div class="page-tab">07</div></div>
</section>

<section class="slide" style="left:49px;top:1402px">
  <svg class="svg-layer" width="712" height="401">
    <circle cx="356" cy="0" r="102" fill="var(--sky)"/>
    <g fill="none" stroke-width="8">
      <circle cx="356" cy="207" r="72" stroke="var(--slate-soft)"/>
      <circle cx="356" cy="207" r="72" stroke="var(--orange)" stroke-dasharray="60 166" transform="rotate(140 356 207)"/>
      <circle cx="356" cy="207" r="72" stroke="var(--orange)" stroke-dasharray="60 392" transform="rotate(-40 356 207)"/>
      <circle cx="356" cy="207" r="72" stroke="var(--cyan)" stroke-dasharray="40 412" transform="rotate(55 356 207)"/>
      <circle cx="356" cy="207" r="72" stroke="var(--cyan)" stroke-dasharray="40 412" transform="rotate(235 356 207)"/>
    </g>
    <g fill="#fff" stroke-width="7">
      <circle cx="303" cy="115" r="35" stroke="var(--cyan)"/>
      <circle cx="409" cy="115" r="35" stroke="var(--slate-soft)"/>
      <circle cx="251" cy="207" r="35" stroke="var(--orange)"/>
      <circle cx="461" cy="207" r="35" stroke="var(--orange)"/>
      <circle cx="303" cy="299" r="35" stroke="var(--slate-soft)"/>
      <circle cx="409" cy="299" r="35" stroke="var(--cyan)"/>
    </g>
    <g fill="none" stroke="#555" stroke-width="1.3">
      <path d="M290 117l8-7 6 3 6-3 8 7-12 8z"/>
      <circle cx="409" cy="113" r="8"/><path d="M405 123h8M406 126h6M405 113l3 3 5-6"/>
      <circle cx="251" cy="207" r="12"/><circle cx="251" cy="207" r="7"/><circle cx="251" cy="207" r="2"/><path d="M251 207l12-10"/>
      <path d="M455 218v-8a9 9 0 1 1 14 4v4"/><circle cx="461" cy="205" r="3"/>
      <path d="M292 308h22M295 306v-8h4v8M301 306v-12h4v12M307 306v-6h4v6M292 297l8-6 5 3 8-6"/>
      <rect x="398" y="293" width="22" height="15"/><path d="M398 293l11 8 11-8M402 288h14v7"/>
    </g>
  </svg>
  <h2 class="heading center" style="top:28px">OUR SOLUTION</h2>
  <div class="sol-title right" style="left:25px;width:200px;top:81px">B2B CONTACT DATA ACQUISITION</div>
  <p class="sol-text right" style="left:90px;top:96px">Lorem ipsum dolor sit amet, consec tetur adipiscing elit, sed do eiusmod tempor incididunt</p>
  <div class="sol-title right" style="left:-18px;width:200px;top:178px">DATA MANAGEMENT</div>
  <p class="sol-text right" style="left:47px;top:193px">Lorem ipsum dolor sit amet, consec tetur adipiscing elit, sed do eiusmod tempor incididunt</p>
  <div class="sol-title right" style="left:27px;width:200px;top:275px">ACCOUNT PROFILING</div>
  <p class="sol-text right" style="left:92px;top:290px">Lorem ipsum dolor sit amet, consec tetur adipiscing elit, sed do eiusmod tempor incididunt</p>
  <div class="sol-title" style="left:485px;top:70px">EFFECTIVE MULTI-CHANNEL<br>DEMAND GENERATION</div>
  <p class="sol-text" style="left:485px;top:100px">Lorem ipsum dolor sit amet, consec tetur adipiscing elit, sed do eiusmod tempor incididunt</p>
  <div class="sol-title" style="left:529px;top:171px">ATTENDEES GENERATION<br>FOR EVENTS</div>
  <p class="sol-text" style="left:529px;top:201px">Lorem ipsum dolor sit amet, consec tetur adipiscing elit, sed do eiusmod tempor incididunt</p>
  <div class="sol-title" style="left:485px;top:275px">BUSINESS PROCESS</div>
  <p class="sol-text" style="left:485px;top:290px">Lorem ipsum dolor sit amet, consec tetur adipiscing elit, sed do eiusmod tempor incididunt</p>
  <div class="footer"><div class="brand">BRELVOXA</div><div class="footer-rule"></div><div class="page-tab">04</div></div>
</section>

<section class="slide" style="left:808px;top:1402px">
  <div class="thanks-band"></div>
  <div class="thanks-word">THANK YOU</div>
  <div class="thanks-art" role="img" aria-label="Isometric illustration of a headset with a red question mark bubble and floating cubes"></div>
  <div class="thanks-pill"></div>
  <svg class="thanks-ico" style="top:192px" width="11" height="11" viewBox="0 0 24 24"><path fill="#fff" d="M6.6 10.8a15 15 0 0 0 6.6 6.6l2.2-2.2c.3-.3.7-.4 1-.2 1.1.4 2.3.6 3.6.6.6 0 1 .4 1 1V20c0 .6-.4 1-1 1A17 17 0 0 1 3 4c0-.6.4-1 1-1h3.5c.6 0 1 .4 1 1 0 1.3.2 2.5.6 3.6.1.3 0 .7-.2 1z"/></svg>
  <div class="thanks-line" style="top:191px">+65 6100 4270</div>
  <svg class="thanks-ico" style="top:219px" width="11" height="9" viewBox="0 0 11 9"><rect width="11" height="9" rx="1" fill="#fff"/><path d="M0.5 1 5.5 5 10.5 1" stroke="var(--slate-dark)" fill="none"/></svg>
  <div class="thanks-line" style="top:217px">enquiries@brelvoxa.com</div>
  <svg class="thanks-ico" style="top:244px" width="11" height="11" viewBox="0 0 12 12"><circle cx="6" cy="6" r="5.5" fill="#fff"/><path d="M1 6h10M6 .5c-3 3-3 8 0 11M6 .5c3 3 3 8 0 11" stroke="var(--slate-dark)" fill="none"/></svg>
  <div class="thanks-line" style="top:243px">www.brelvoxa.com</div>
  <svg class="thanks-ico" style="top:270px" width="9" height="12" viewBox="0 0 9 12"><path d="M4.5 0a4.5 4.5 0 0 1 4.5 4.5C9 8 4.5 12 4.5 12S0 8 0 4.5A4.5 4.5 0 0 1 4.5 0z" fill="#fff"/><circle cx="4.5" cy="4.5" r="1.6" fill="var(--slate-dark)"/></svg>
  <div class="thanks-line" style="top:269px">8 Quayside Lane, #04-12<br>Keppel Point,<br>Singapore 090118</div>
  <div class="footer"><div class="brand">BRELVOXA</div><div class="footer-rule"></div><div class="page-tab">08</div></div>
</section>

<section class="slide" style="left:429px;top:1861px">
  <h2 class="abs" style="left:0;width:712px;top:24px;text-align:center;font-size:22px;font-weight:500;letter-spacing:.4px">TITLE HERE</h2>
  <div class="footer"><div class="brand">BRELVOXA</div><div class="footer-rule"></div><div class="page-tab">09</div></div>
</section>

</div>
</body>
</html>
```